Children's Chorus Flyer

Hello,

I need a flyer design (probably in two sizes 8x11, 5x7) that promotes my community children's chorus and also announces our summer camp. I would like a flyer that is playful and eye-catching while remaining somewhat simplistic. It should have our logo (will upload that) and either some cartoon graphics or pictures of the current kids or both. Although it does not have to have the picture of the kids. I'm leaving it up to you. I am uploading an example of a flyer that I like to help guide you. It needs to have this basic info:

"Do you love to sing? The Meadowlark Singers is looking for boys and girls ages 7-16 to audition for the 2012-2013 season! Rehearsals are held weekly at Birchfield Grove Methodist Church (27815 Hennaway Ln). Contact us for an audition appointment.

Summer Choral Camp!
The Meadowlark Singers is planning a 2-week choral camp where singers will have fun working on music reading skills, vocal technique, choreography and more! Boys and girls ages 7-16 are invited to enroll.

Dates: July 16-27
Times: 9am-3pm (extended care hours available at additional fee)
Tuition: $300 for 2-week session ($150 per week)

For more information, please visit our website: www.meadowlarksingers.org, email: info@meadowlarksingers.org or call 555.384.9127."

Target Market(s)

parents and children

Industry/Entity Type

Church

Requirements
Must have
• logo, basic info typed above.
Nice to have
• the picture of the kids, although not totally necessary. Leaving it up to your creative ideas.

```html
<!DOCTYPE html>
<html lang="en">
<head>
<meta charset="utf-8">
<title>The Meadowlark Singers – Auditions &amp; Summer Choral Camp</title>
<link href="https://fonts.googleapis.com/css2?family=Cherry+Swash:wght@700&family=Noto+Sans+Mono:wght@600;700;800&family=Marck+Script&display=swap" rel="stylesheet">
<style>
  :root {
    --teal: #0f9591;
    --teal-dark: #0b7a77;
    --yellow-line: #f3ef5a;
    --note-box: #fbfb6e;
    --ink: #111111;
    --red: #e3101a;
    --glow: #d4f3fb;
    --url-green: #9bd43a;
    --logo-teal: #4f9e9a;
    --photo-a: #c9b8a6;
    --photo-b: #5b4a40;
    --kid-a: #fbe9d7;
    --kid-b: #e8c07a;
  }
  * { box-sizing: border-box; margin: 0; padding: 0; }
  html, body { width: 857px; height: 1200px; overflow: hidden; background: #fff; }
  .flyer { position: relative; width: 857px; height: 1200px; background: #fff; color: var(--ink);
    font-family: "Noto Sans Mono", monospace; overflow: hidden; }

  .band { position: absolute; left: 0; width: 100%; background: var(--teal); }
  .band--top { top: 0; height: 32px; }
  .band--mid-a { top: 232px; height: 17px; }
  .band--mid-line { top: 249px; height: 5px; background: var(--yellow-line); }
  .band--mid-b { top: 254px; height: 16px; }

  .logo { position: absolute; left: 40px; top: 32px; width: 380px; height: 200px;
    display: flex; align-items: center; gap: 14px; }
  .logo__dot { width: 26px; height: 26px; border-radius: 50%; background: var(--logo-teal); flex: none; }
  .logo__name { font-weight: 700; font-size: 34px; line-height: 1.15; color: var(--logo-teal); }

  .chorus-photo { position: absolute; left: 444px; top: 32px; width: 372px; height: 200px;
    background: linear-gradient(180deg, var(--photo-a), var(--photo-b)); }

  .glow { position: absolute; border-radius: 50%;
    background: radial-gradient(circle, var(--glow) 0%, rgba(212,243,251,0) 70%); }

  .headline { position: absolute; left: 0; width: 100%; text-align: center;
    font-family: "Cherry Swash", cursive; font-weight: 700; color: #0c2a2a;
    text-shadow: 0 0 3px var(--teal), 0 0 6px #6fe0e0, 0 0 2px #fff; }
  .headline--audition { top: 296px; font-size: 41px; }
  .headline--camp { top: 688px; font-size: 32px; }

  .audition-lead { position: absolute; top: 366px; left: 0; width: 100%; text-align: center;
    font-size: 24px; font-weight: 700; line-height: 31px; }
  .audition-details { position: absolute; top: 433px; left: 0; width: 100%; text-align: center;
    font-size: 13px; font-weight: 700; line-height: 17px; }

  .kid { position: absolute; top: 492px; height: 156px; border-radius: 50% 50% 12px 12px;
    background: linear-gradient(180deg, var(--kid-a), var(--kid-b)); }
  .kid--boy { left: 203px; width: 140px; }
  .kid--girl { left: 472px; width: 165px; }

  .camp-text { position: absolute; top: 741px; left: 0; width: 100%; text-align: center;
    font-size: 21px; font-weight: 700; line-height: 28px; }

  .camp-facts { position: absolute; left: 67px; top: 865px; width: 720px; height: 152px;
    background: var(--note-box); padding: 18px 0 0 36px; }
  .camp-facts__row { font-size: 20px; font-weight: 700; line-height: 36px; white-space: nowrap; }
  .camp-facts__label { color: var(--red); font-size: 25px; }
  .camp-facts__note { font-size: 14px; }

  .closing { position: absolute; top: 1028px; left: 0; width: 100%; text-align: center;
    font-family: "Marck Script", cursive; font-size: 50px; }
  .contact { position: absolute; left: 0; width: 100%; text-align: center; font-weight: 700; }
  .contact--intro { top: 1128px; font-size: 14px; }
  .contact--web { top: 1144px; font-size: 29px; font-weight: 800; color: var(--url-green);
    -webkit-text-stroke: 1px #1a3a1a; text-shadow: 0 0 4px var(--teal); }
  .contact--mail { top: 1180px; font-size: 14px; }
</style>
</head>
<body>
<main class="flyer">
  <div class="band band--top"></div>

  <header class="logo">
    <span class="logo__dot"></span>
    <span class="logo__name">The Meadowlark Singers</span>
  </header>
  <div class="chorus-photo" role="img" aria-label="Photo of the chorus children in white shirts and blue scarves cheering"></div>

  <div class="band band--mid-a"></div>
  <div class="band band--mid-line"></div>
  <div class="band band--mid-b"></div>

  <div class="glow" role="img" aria-label="Music note" style="left:20px;top:270px;width:120px;height:120px"></div>
  <div class="glow" role="img" aria-label="Music note" style="left:730px;top:270px;width:120px;height:120px"></div>
  <div class="glow" role="img" aria-label="Music note" style="left:90px;top:470px;width:110px;height:110px"></div>
  <div class="glow" role="img" aria-label="Music note" style="left:670px;top:470px;width:120px;height:110px"></div>

  <h1 class="headline headline--audition">Do You Love To Sing?</h1>
  <p class="audition-lead">The Meadowlark Singers is looking for boys and girls<br>ages 7-16 to audition for the 2012-2013 season!</p>
  <p class="audition-details">Reherasals are held weekly at Birchfield Grove Methodist Church on 27815 Hennaway Ln.<br>Contact us for audition appointment.</p>

  <div class="kid kid--boy" role="img" aria-label="Cartoon boy singing from a songbook"></div>
  <div class="kid kid--girl" role="img" aria-label="Cartoon girl singing from a songbook"></div>

  <h2 class="headline headline--camp">Announcing our Summer Choral camp!</h2>
  <p class="camp-text">The Meadowlark Singers is planning a 2-week choral camp where<br>singers will have fun working on music reading skills,<br>vocal technique, choreography and more.<br>Boys and girls ages 7-16 are invited to enroll</p>

  <section class="camp-facts">
    <p class="camp-facts__row"><span class="camp-facts__label">Dates:</span> July 16-27</p>
    <p class="camp-facts__row"><span class="camp-facts__label">Times:</span> 9am-3pm <span class="camp-facts__note">(extended care hours available at additional fee)</span></p>
    <p class="camp-facts__row"><span class="camp-facts__label">Tuition:</span>$300 for a 2-week session ($150 per week)</p>
  </section>

  <p class="closing">Come sing with us!</p>
  <p class="contact contact--intro">For more information, please visit our website:</p>
  <p class="contact contact--web">www.meadowlarksingers.org</p>
  <p class="contact contact--mail">Email: info@meadowlarksingers.org or call 555-384-9127</p>
</main>
</body>
</html>
```